Kestrel Business Accountants , logo & business card design

I am a business consultant & accountant , servicing a range of small business clients , providing business & taxation advice.
I am looking for a logo & business card design that is not traditional accounting style.
Something colorful & innovative would be good.
Target Market(s)
Small businesses in their growth stage
Industry/Entity Type
Business Consultant
Contact Information for Business Card
Kestrel Business Accountants Pty Ltd
Miles Hartley CPA
Director
Ph: 0413 8064 91
Email : kestrel@pallinet.com.au
On reverse of card:
"Kestrel Sight for your Business"
Business Consulting
Taxation
Superannuation
Logo styles of interest
Abstract Logo
Wordmark Logo
Look and feel

```html
<!DOCTYPE html>
<html lang="en">
<head>
<meta charset="utf-8">
<title>Kestrel Business Accountants – Business Card</title>
<link href="https://fonts.googleapis.com/css2?family=Montserrat:wght@300;400&display=swap" rel="stylesheet">
<style>
  :root {
    --page: #ffffff;
    --card: #ffffff;
    --ink: #111111;
    --ink-soft: #2a2a2a;
    --accent: #f0432a;
    --gold-pale-1: #f6eeb4;
    --gold-pale-2: #e6d68a;
    --gold-1: #f3e36a;
    --gold-2: #c9a72a;
    --shadow: rgba(0, 0, 0, 0.55);
  }
  * { box-sizing: border-box; margin: 0; padding: 0; }
  html, body { width: 1200px; height: 1000px; overflow: hidden; background: var(--page); }
  body { position: relative; font-family: "Montserrat", sans-serif; color: var(--ink); }

  .card {
    position: absolute;
    left: 303px;
    width: 584px;
    height: 337px;
    background: var(--card);
    box-shadow: 8px 8px 10px var(--shadow);
    overflow: hidden;
  }
  .card--front { top: 105px; }
  .card--back { top: 526px; }

  .ornament {
    position: absolute;
    left: 37px;
    width: 515px;
    border-radius: 50% 50% 46% 46% / 40% 40% 60% 60%;
  }
  .card--front .ornament {
    top: 135px; height: 192px;
    background: radial-gradient(ellipse at 50% 70%, var(--gold-pale-2), var(--gold-pale-1) 55%, rgba(246,238,180,0) 78%);
    opacity: 0.75;
  }
  .card--back .ornament {
    top: 134px; height: 194px;
    background: radial-gradient(ellipse at 50% 70%, var(--gold-2), var(--gold-1) 55%, rgba(243,227,106,0) 78%);
    opacity: 0.8;
  }

  .brand {
    position: absolute;
    left: 0; right: 0;
    text-align: center;
  }
  .brand__name {
    display: inline-flex;
    align-items: center;
    gap: 14px;
    font-weight: 300;
    color: var(--ink);
    line-height: 1;
  }
  .brand__dot { border-radius: 50%; background: var(--accent); display: inline-block; }
  .brand__tagline { color: var(--accent); font-weight: 300; line-height: 1; }

  .card--front .brand { top: 44px; }
  .card--front .brand__name { font-size: 80px; }
  .card--front .brand__dot { width: 30px; height: 30px; }
  .card--front .brand__tagline { font-size: 19px; margin-top: 12px; }

  .card--back .brand { top: 40px; }
  .card--back .brand__name { font-size: 64px; gap: 11px; }
  .card--back .brand__dot { width: 24px; height: 24px; }
  .card--back .brand__tagline { font-size: 14.5px; margin-top: 9px; }

  .contact {
    position: absolute;
    top: 197px; left: 0; right: 0;
    text-align: center;
    font-size: 12.5px;
    line-height: 16.5px;
    color: var(--ink-soft);
    font-weight: 400;
  }

  .slogan {
    position: absolute;
    top: 160px; left: 0; right: 0;
    text-align: center;
  }
  .slogan__quote { font-size: 22px; font-weight: 400; color: var(--ink); line-height: 1.1; }
  .slogan__services { font-size: 12.5px; color: var(--ink-soft); margin-top: 3px; }
</style>
</head>
<body>
  <section class="card card--front" aria-label="Business card front">
    <div class="ornament" role="img" aria-label="Gold flourish ornament of curling leaves"></div>
    <div class="brand">
      <div class="brand__name"><span>Kestrel</span><span class="brand__dot"></span></div>
      <div class="brand__tagline">Business Accountants Pty Ltd</div>
    </div>
    <address class="contact" style="font-style: normal;">
      <p>Kestrel Business Accountants Pty Ltd</p>
      <p>Miles Hartley</p>
      <p>CPA Director</p>
      <p>Ph: 0413 8064 91</p>
      <p>Email : kestrel@pallinet.com.au</p>
    </address>
  </section>

  <section class="card card--back" aria-label="Business card back">
    <div class="ornament" role="img" aria-label="Gold flourish ornament of curling leaves"></div>
    <div class="brand">
      <div class="brand__name"><span>Kestrel</span><span class="brand__dot"></span></div>
      <div class="brand__tagline">Business Accountants Pty Ltd</div>
    </div>
    <div class="slogan">
      <p class="slogan__quote">"Kestrel Sight for your Business"</p>
      <p class="slogan__services">Business Consulting Taxation Superannuation</p>
    </div>
  </section>
</body>
</html>
```